Logo & Responsive Website Design for Mortgage Company

Vantor Mortgage is a new Mortgage Fin-Tech company that will use its own innovative, proprietary technology for lead generation, mortgage origination, and processing of residential home loans in the US. The design should convey that we are a technology-driven company, offering borrowers seeking home loans an exceptional experience throughout the borrowing process.

We are looking for designs that are elegant, convey technical competency, simple to navigate, and set us apart from the competition.

We are not set on any particular colors at this point, so feel free to choose the best colors for your particular designs.

Please include both desktop and mobile designs.

Some Examples of Mortgage Websites. These are to show the typical content, not designs that we particularly like or dislike.
https://www.plumvane.com/
https://www.qbtfunding.com/
https://dorvelmortgage.com/
https://kelvo.com/
https://corvabaylending.com/

Please send comments with additional questions.

Thank You For your participation.

Target Market(s)

U.S. Residential Home Loan Seekers

Industry/Entity Type

FinTech Mortgage

Number of Pages Required

2 page

```html
<!DOCTYPE html>
<html lang="en">
<head>
<meta charset="utf-8">
<title>Vantor Mortgage</title>
<link href="https://fonts.googleapis.com/css2?family=Poppins:wght@400;500;600;700;800&family=Playfair+Display:ital,wght@1,700&display=swap" rel="stylesheet">
<style>
:root{
  --blue:#2a9fc4;
  --blue-hero:#24a8c9;
  --blue-deep:#1d89ad;
  --navy:#0f2d45;
  --navy-band:#0e3550;
  --orange:#f7830f;
  --grey-panel:#ebebeb;
  --grey-light:#f2f2f2;
  --ink:#2b2b2b;
  --white:#ffffff;
}
*{margin:0;padding:0;box-sizing:border-box}
html,body{width:1200px;height:3459px;overflow:hidden;background:var(--white)}
body{position:relative;font-family:'Poppins',sans-serif;color:var(--ink)}
.abs{position:absolute}
.photo{position:absolute}

/* header */
.site-header{position:absolute;left:0;top:0;width:1200px;height:112px;background:var(--white);border-bottom:2px solid var(--blue)}
.brand{position:absolute;left:138px;top:48px;display:flex;align-items:center;gap:8px;font-size:15px;font-weight:600;color:var(--blue)}
.brand .dot{width:22px;height:22px;border-radius:50%;background:var(--blue)}
.nav a{position:absolute;top:45px;font-size:19px;font-weight:500;color:#333;text-decoration:none}
.nav a.active{color:var(--blue)}
.login{position:absolute;left:878px;top:36px;width:119px;height:42px;border-radius:21px;background:var(--blue);color:#fff;font-size:18px;font-weight:500;display:flex;align-items:center;justify-content:center;box-shadow:0 3px 6px rgba(0,0,0,.25)}
.social{position:absolute;top:38px;width:32px;height:32px;border-radius:50%;background:var(--blue)}

/* hero */
.hero{position:absolute;left:0;top:112px;width:1200px;height:708px;background:linear-gradient(135deg,#2ab4d4,#1f8fb4)}
.hero h1{position:absolute;left:138px;top:140px;font-size:60px;line-height:80px;color:#fff;font-weight:500}
.hero h1 b{font-weight:800}
.btn-start{position:absolute;left:126px;top:416px;width:172px;height:45px;border-radius:23px;background:#fff;color:#222;font-size:17px;font-weight:500;display:flex;align-items:center;justify-content:center;gap:8px}

/* about */
.about-panel{position:absolute;left:0;top:928px;width:1090px;height:610px;background:var(--grey-panel);border-radius:0 40px 40px 0}
.about h2{position:absolute;left:601px;top:967px;font-size:54px;font-weight:700;color:var(--navy)}
.about h2 span{color:var(--blue)}
.about h3{position:absolute;left:604px;top:1040px;font-size:33px;font-weight:500;color:#333}
.about p{position:absolute;left:606px;top:1094px;width:410px;font-size:21px;line-height:33px;color:#333}
.btn-orange{position:absolute;background:var(--orange);color:#fff;font-weight:500;display:flex;align-items:center;justify-content:center;gap:8px}

/* unique */
.unique{position:absolute;left:0;top:1597px;width:1200px;height:599px;background:linear-gradient(180deg,#2ba2c6 0%,#2d9ec0 60%,#3aa8c6 100%)}
.unique h2{position:absolute;left:0;width:1200px;top:55px;text-align:center;font-size:56px;font-weight:700;color:#fff}
.unique h2 em{font-family:'Playfair Display',serif;color:var(--navy);text-decoration:underline;text-decoration-thickness:3px;text-underline-offset:8px}
.unique .lead{position:absolute;left:0;width:1200px;top:146px;text-align:center;font-size:27px;color:#fff}
.pillar{position:absolute;top:240px;width:253px;height:255px;background:#f2f2f2;border-radius:24px;text-align:center;box-shadow:0 4px 10px rgba(0,0,0,.15)}
.pillar .icon{width:90px;height:90px;border-radius:50%;background:var(--orange);margin:16px auto 0;display:flex;align-items:center;justify-content:center}
.pillar h4{margin-top:28px;font-size:20px;font-weight:600;color:var(--orange)}
.pillar p{margin-top:6px;font-size:17px;line-height:20px;color:#222}
.pillar small{display:block;margin-top:14px;font-size:11px;color:var(--orange)}

/* news */
.news-title{position:absolute;left:0;width:1200px;top:2240px;text-align:center;font-size:43px;font-weight:700;color:var(--navy)}
.news-lead{position:absolute;left:0;width:1200px;top:2305px;text-align:center;font-size:22px;color:#222}
.news-band{position:absolute;left:0;top:2360px;width:1200px;height:258px;background:var(--grey-light)}
.news-card{position:absolute;top:2393px;width:260px;height:180px;display:flex}
.news-card .pic{width:106px;height:180px}
.news-card .body{margin-left:6px;width:148px;height:180px;background:#2c2c2a;color:#fff;text-align:center;padding-top:18px}
.news-card.light .body{background:#fff;color:#222;box-shadow:0 2px 6px rgba(0,0,0,.15)}
.news-card h5{font-size:16px;font-weight:500}
.news-card p{font-size:12px;line-height:20px;margin-top:6px;padding:0 6px}
.news-card small{display:block;margin-top:14px;font-size:8px;font-weight:600}
.arrow{position:absolute;width:25px;height:25px;border-radius:50%;display:flex;align-items:center;justify-content:center}

/* connect */
.connect{position:absolute;left:0;top:2665px;width:606px;height:472px;background:var(--grey-light)}
.connect h2{position:absolute;left:0;width:606px;top:20px;text-align:center;font-size:43px;font-weight:700;color:#333}
.connect .sub{position:absolute;left:0;width:606px;top:82px;text-align:center;font-size:17px;font-weight:500;color:#222}
.field{position:absolute;background:#fff;border-radius:8px;font-size:11px;color:#444;padding:18px 0 0 17px}
.whatwedo{position:absolute;left:606px;top:2665px;width:594px;height:472px;background:linear-gradient(160deg,#2fa6c8,#2796bb)}
.whatwedo h2{position:absolute;left:0;width:594px;top:58px;text-align:center;font-size:42px;font-weight:600;color:#fff}
.whatwedo .rule{position:absolute;left:139px;top:120px;width:113px;height:2px;background:#fff}
.whatwedo p{position:absolute;left:55px;width:484px;top:148px;text-align:center;font-size:17px;line-height:30px;color:#fff}
.btn-work{position:absolute;left:206px;top:337px;width:150px;height:28px;background:#fff;color:var(--navy);font-size:18px;font-weight:600;display:flex;align-items:center;justify-content:center}

/* newsletter */
.newsletter{position:absolute;left:0;top:3137px;width:1200px;height:92px;background:var(--navy-band)}
.newsletter .label{position:absolute;left:298px;top:36px;display:flex;align-items:center;gap:14px;color:#fff;font-size:16px;font-weight:600}
.newsletter .input{position:absolute;left:596px;top:33px;width:281px;height:35px;background:#fff;border-radius:6px;font-size:11px;color:#444;padding:11px 0 0 22px}

/* footer */
.footer{position:absolute;left:0;top:3229px;width:1200px;height:230px;background:var(--blue)}
.footer .brand-foot{position:absolute;left:206px;top:110px;font-size:17px;font-weight:600;color:#fff;display:flex;align-items:center;gap:8px}
.footer .brand-foot .dot{width:22px;height:22px;border-radius:50%;background:#fff}
.footer h6{position:absolute;font-size:15px;font-weight:500;color:#fff}
.footer .line{position:absolute;font-size:12px;font-weight:500;color:#fff;display:flex;align-items:center;gap:10px}
.footer .copy{position:absolute;left:0;width:1200px;top:192px;text-align:center;font-size:12px;color:#fff;font-weight:500}
</style>
</head>
<body>

<header class="site-header">
  <div class="brand"><span class="dot"></span>Vantor Mortgage</div>
  <nav class="nav">
    <a class="active" style="left:438px">Home</a>
    <a style="left:536px">About us</a>
    <a style="left:662px">Blog</a>
    <a style="left:746px">More
      <svg width="16" height="10" viewBox="0 0 16 10" style="margin-left:6px"><path d="M2 2l6 6 6-6" fill="none" stroke="#2a9fc4" stroke-width="2"/></svg></a>
  </nav>
  <div class="login">LOG IN</div>
  <div class="social" style="left:1053px"></div>
  <div class="social" style="left:1111px"></div>
</header>

<section class="hero">
  <svg class="photo" width="1200" height="708" style="left:0;top:0" role="img" aria-label="Photo of a hand holding a small model house with keys above a notebook and documents on a desk">
    <defs>
      <linearGradient id="heroPhoto" x1="0" y1="0" x2="1" y2="1">
        <stop offset="0" stop-color="#d9e8ee"/>
        <stop offset=".5" stop-color="#c7d3d8"/>
        <stop offset="1" stop-color="#8fa4ad"/>
      </linearGradient>
    </defs>
    <polygon points="660,0 1200,0 1018,708 452,708" fill="url(#heroPhoto)"/>
  </svg>
  <h1>Vantor Mortgage<br>Fin-Tech<br><b>company.</b></h1>
  <div class="btn-start">Get Started
    <svg width="14" height="12" viewBox="0 0 14 12"><path d="M1 6h11M7 1l5 5-5 5" fill="none" stroke="#222" stroke-width="2"/></svg></div>
</section>

<section class="about">
  <div class="about-panel"></div>
  <div class="photo" style="left:55px;top:872px;width:275px;height:575px;background:linear-gradient(180deg,#e9ecee,#d6d9db)" role="img" aria-label="Portrait photo of a smiling woman with glasses holding a laptop"></div>
  <div class="photo" style="left:343px;top:872px;width:219px;height:575px;background:linear-gradient(180deg,#e4e9ec,#b9c0c4)" role="img" aria-label="Portrait photo of a smiling man in a grey blazer"></div>
  <h2>About <span>Us</span></h2>
  <h3>Who We Are ?</h3>
  <p>Lorem Ipsum is simply dummy text of the printing and typesetting industry. Lorem Ipsum has been the industry's standard dummy text ever since the 1500s, when an unknown printer took a galley of type and scrambled it to make a type specimen book.</p>
  <div class="btn-orange" style="left:608px;top:1370px;width:172px;height:46px;border-radius:23px;font-size:17px">LEARN MORE
    <svg width="14" height="12" viewBox="0 0 14 12"><path d="M1 6h11M7 1l5 5-5 5" fill="none" stroke="#fff" stroke-width="2"/></svg></div>
</section>

<section class="unique">
  <h2>What Makes Us <em>Unique.</em></h2>
  <div class="lead">Vantor Mortgage company focused on the three pillars of IT Security</div>
  <div class="pillar" style="left:150px">
    <div class="icon"><svg width="44" height="44" viewBox="0 0 44 44" fill="none" stroke="#fff" stroke-width="2"><rect x="8" y="4" width="22" height="30" rx="2"/><rect x="24" y="24" width="14" height="12" rx="2"/><path d="M27 24v-4a4 4 0 0 1 8 0v4"/></svg></div>
    <h4>CONFIDENTIALITY</h4>
    <p>It has survived not<br>only five centuries,</p>
    <small>LEARN MORE...</small>
  </div>
  <div class="pillar" style="left:470px">
    <div class="icon"><svg width="44" height="44" viewBox="0 0 44 44" fill="none" stroke="#fff" stroke-width="2"><circle cx="22" cy="22" r="12"/><circle cx="22" cy="22" r="5"/><path d="M22 4v6M22 34v6M4 22h6M34 22h6"/></svg></div>
    <h4>INTEGRITY</h4>
    <p>It has survived not<br>only five centuries,</p>
    <small>LEARN MORE...</small>
  </div>
  <div class="pillar" style="left:790px">
    <div class="icon"><svg width="50" height="50" viewBox="0 0 50 50" fill="none" stroke="#fff" stroke-width="3"><circle cx="25" cy="25" r="18"/><path d="M25 13v12l8 5"/></svg></div>
    <h4>AVAILABILITY</h4>
    <p>It has survived not<br>only five centuries,</p>
    <small>LEARN MORE...</small>
  </div>
</section>

<h2 class="news-title">Latest News</h2>
<div class="news-lead">Lorem Ipsum is simply dummy text of the printing</div>
<div class="news-band"></div>
<div class="arrow" style="left:86px;top:2479px;background:var(--orange)"><svg width="10" height="10" viewBox="0 0 10 10"><path d="M6.5 1.5L3 5l3.5 3.5" fill="none" stroke="#fff" stroke-width="1.8"/></svg></div>
<div class="arrow" style="left:1087px;top:2477px;background:var(--navy)"><svg width="10" height="10" viewBox="0 0 10 10"><path d="M3.5 1.5L7 5 3.5 8.5" fill="none" stroke="#fff" stroke-width="1.8"/></svg></div>
<article class="news-card" style="left:154px">
  <div class="pic" style="background:linear-gradient(180deg,#d8dde2,#8d96a0)" role="img" aria-label="Photo of a woman writing in a notebook"></div>
  <div class="body"><h5>Work Freaks</h5><p>Lorem Ipsum is simply dummy text of the printing and typesetting industry.</p><small>READ MORE</small></div>
</article>
<article class="news-card" style="left:467px">
  <div class="pic" style="background:linear-gradient(180deg,#9fb7cc,#3f5566)" role="img" aria-label="Photo of people working in a bright office"></div>
  <div class="body"><h5>Today Job !</h5><p>Lorem Ipsum is simply dummy text of the printing and typesetting industry.</p><small>READ MORE</small></div>
</article>
<article class="news-card light" style="left:780px">
  <div class="pic" style="background:linear-gradient(180deg,#c9a98a,#e8e4df)" role="img" aria-label="Photo of a person typing on a laptop"></div>
  <div class="body"><h5>Employee</h5><p>Lorem Ipsum is simply dummy text of the printing and typesetting industry.</p><small>READ MORE</small></div>
</article>

<section class="connect">
  <h2>Lets Connect</h2>
  <div class="sub">TO DISCUSS YOUR BUSINESS NEEDS</div>
  <div class="field" style="left:108px;top:135px;width:196px;height:40px;padding-top:14px">First Name</div>
  <div class="field" style="left:324px;top:135px;width:196px;height:40px;padding-top:14px">Last Name</div>
  <div class="field" style="left:108px;top:201px;width:412px;height:40px;padding-top:14px">Phone No</div>
  <div class="field" style="left:108px;top:262px;width:412px;height:123px">Message</div>
  <div class="btn-orange" style="left:243px;top:412px;width:101px;height:23px;border-radius:4px;font-size:14px">Submit</div>
</section>

<section class="whatwedo">
  <h2>What We Do ?</h2>
  <div class="rule"></div>
  <p>Lorem Ipsum is simply dummy text of the printing and typesetting industry. Lorem Ipsum has been the industry's standard dummy text ever since the 1500s, when an unknown printer took a galley of type and scrambled it to make a type specimen book.</p>
  <div class="btn-work">See Our Work</div>
</section>

<section class="newsletter">
  <div class="label"><svg width="24" height="22" viewBox="0 0 24 22" fill="none" stroke="#fff" stroke-width="1.8"><path d="M22 2L2 10l7 3 2 7 3-5 5 3z"/><path d="M9 13L22 2"/></svg>SUBSCRIBE FOR NEWSLETTER</div>
  <div class="input">Your Email Address</div>
</section>

<footer class="footer">
  <div class="brand-foot"><span class="dot"></span>VANTOR MORTGAGE</div>
  <h6 style="left:514px;top:52px">CONTACT US</h6>
  <div class="line" style="left:492px;top:89px"><svg width="12" height="9" viewBox="0 0 12 9"><rect x=".5" y=".5" width="11" height="8" fill="none" stroke="#fff"/><path d="M.5.5L6 5 11.5.5" fill="none" stroke="#fff"/></svg>HELLO@VANTORMORTGAGE.COM</div>
  <div class="line" style="left:492px;top:121px"><svg width="12" height="12" viewBox="0 0 12 12"><path d="M2 1l3 1-1 3 3 3 3-1 1 3-2 1C5 11 1 7 1 3z" fill="#fff"/></svg>01632 960418</div>
  <h6 style="left:800px;top:40px">VISIT US</h6>
  <div class="line" style="left:778px;top:75px"><svg width="10" height="13" viewBox="0 0 10 13"><path d="M5 12C2 8 1 6 1 4.5a4 4 0 0 1 8 0C9 6 8 8 5 12z" fill="#fff"/><circle cx="5" cy="4.5" r="1.5" fill="var(--blue)"/></svg>48 HARLOW QUAY STREET,</div>
  <div class="line" style="left:800px;top:108px">LARKFIELD, DUBLIN 6, D06 PL42</div>
  <div class="copy">© copyrights 2022 Vantor Mortgage | &nbsp;All Rights Reserved</div>
</footer>

</body>
</html>
```